Task Description:
I’m wanting a professionally designed 8 ½' x 11, 3 fold brochure, both sides, to print as my target audience are those people who primarily don’t have access to the internet. These items will be dropped off in the mailboxes of all households in the city.
However I do have a web site www.civicharborvote.ca where I would like to have it as a document that can be down loaded.
This is my first foray into political office and my message needs to be clear, concise and easy to understand. The brochure should be a bit conservative yet be warm and inviting. I’ve selected two pictures that I think make sense under their respective headings, but I'm open to suggestions.I need to update my picture for the front cover.
There is the possibility of having T shirts and business cards made up, which would be in essence a simpler version of the brochure so please keep this in mind. I ask that you work with me and I will compensate you accordingly for the extras should they be required. You may want to consider making the Civic Harbor Vote into a logo as we own all the web extensions and have applied for copyright protection for branding purposes.
You may want to look at QL Brightmoor http://www.qlbrightmoor.ca/ , or the Silver Pine Trust of Canada www.silverpinetrust.com as two recognizable colour schemes here in Canada but don’t let that limit your imagination.
The content in the flier should remain intact although I am open to some minor suggestions. As you can see my talents as a graphic artist are limited hence my need for that professional make over that will give it a bit of razzle dazzle and set me out from the other candidates. So use your imagination!!
Target Market(s)
Middle age voters who may or may not have access to the internet and still prefer print
Industry/Entity Type
Conservative
Look and feel

```html
<!DOCTYPE html>
<html lang="en">
<head>
<meta charset="utf-8">
<title>Civic Harbor Vote – Brochure Panel</title>
<link href="https://fonts.googleapis.com/css2?family=Source+Sans+3:wght@400;600;700&display=swap" rel="stylesheet">
<style>
  :root {
    --band-blue: #4a5cab;
    --rule-blue: #4256a3;
    --paper: #ffffff;
    --sepia-light: #f1e8e1;
    --sepia-mid: #e2cfc1;
    --sepia-deep: #cfb19d;
    --ink: #1d1a18;
    --heading-white: #ffffff;
  }
  * { box-sizing: border-box; margin: 0; padding: 0; }
  html, body { width: 1200px; height: 908px; overflow: hidden; background: var(--paper); }
  body { font-family: "Source Sans 3", "Myriad Pro", sans-serif; color: var(--ink); }

  .brochure { position: relative; width: 1200px; height: 908px; overflow: hidden; background: var(--paper); }

  .top-band { position: absolute; left: 0; top: 0; width: 1200px; height: 116px; background: var(--band-blue); }
  .top-rule { position: absolute; left: 0; top: 122px; width: 1200px; height: 5px; background: var(--rule-blue); }

  .backdrop-photo {
    position: absolute; left: 0; top: 132px; width: 1200px; height: 705px;
    background:
      radial-gradient(ellipse 260px 300px at 250px 260px, rgba(250,243,238,0.85), transparent 70%),
      radial-gradient(ellipse 240px 320px at 600px 330px, rgba(245,236,229,0.8), transparent 70%),
      radial-gradient(ellipse 300px 360px at 980px 300px, rgba(236,222,211,0.7), transparent 70%),
      linear-gradient(100deg, var(--sepia-light) 0%, var(--sepia-mid) 45%, var(--sepia-deep) 100%);
  }

  .bottom-rule { position: absolute; left: 0; top: 840px; width: 1200px; height: 5px; background: var(--rule-blue); }
  .bottom-band { position: absolute; left: 0; top: 851px; width: 1200px; height: 57px; background: var(--band-blue); }

  .panel-title {
    position: absolute; color: var(--heading-white); font-weight: 600;
    font-size: 34px; line-height: 1; letter-spacing: 0.2px; white-space: nowrap;
  }
  .title-economy { left: 61px; top: 46px; }
  .title-community { left: 866px; top: 46px; }
  .title-opportunities { left: 421px; top: 30px; }
  .title-beginnings { left: 523px; top: 74px; }

  .panel-copy {
    position: absolute; width: 292px; font-size: 15.9px; line-height: 21.4px;
    text-align: justify;
  }
  .panel-copy p { margin-bottom: 21.4px; }
  .copy-economy { left: 65px; top: 180px; }
  .copy-opportunities { left: 460px; top: 183px; }
  .copy-community { left: 863px; top: 183px; }
  .copy-community strong { font-weight: 700; }

  .open-for-business {
    position: absolute; left: 428px; top: 795px; width: 340px; text-align: center;
    font-weight: 700; font-size: 18.5px;
  }

  .family-photo {
    position: absolute; left: 897px; top: 609px; width: 224px; height: 169px;
    background: #fff; padding: 5px;
  }
  .family-photo-fill {
    width: 100%; height: 100%;
    background: linear-gradient(160deg, #3a3d44 0%, #22252b 55%, #4a4a4f 100%);
  }
  .photo-caption {
    position: absolute; left: 880px; top: 792px; width: 258px; text-align: center;
    font-size: 14.5px;
  }

  .site-link {
    position: absolute; top: 866px; width: 300px; text-align: center;
    color: var(--heading-white); font-size: 18.5px;
  }
  .link-left { left: 60px; }
  .link-middle { left: 448px; }
  .link-right { left: 850px; }
</style>
</head>
<body>
<main class="brochure">
  <div class="top-band"></div>
  <div class="top-rule"></div>
  <div class="backdrop-photo" role="img" aria-label="Faded sepia photograph of a smiling family group spanning the panels"></div>
  <div class="bottom-rule"></div>
  <div class="bottom-band"></div>

  <h2 class="panel-title title-economy">A Strong Economy</h2>
  <h1 class="panel-title title-opportunities">New Opportunities</h1>
  <h1 class="panel-title title-beginnings">New Beginnings</h1>
  <h2 class="panel-title title-community">A Safe Community</h2>

  <section class="panel-copy copy-economy">
    <p>Without a strong economy we can’t afford to pay for social services that we now take for granted.</p>
    <p>&nbsp;&nbsp;Although the City is the largest corporation it is unique in the fact that it revenue stream is tied directly to taxation</p>
    <p>&nbsp;Without new business and new citizens the burden of taxes will fall increasingly on residential taxpayers.</p>
    <p>&nbsp;Our demographics have changed over the years and those changes need to be reflected in the way we tax our citizens.</p>
    <p>&nbsp;Our levels of debts and our future commitments need to be effectively communicated to the people that own this city. You the tax payer!!</p>
    <p>&nbsp;Currently our debt is 178 million dollars with further commitments of 153 million for homes for the aged and the possibility of 100 million dollar multi purpose facility. How will we pay for this?</p>
  </section>

  <section class="panel-copy copy-opportunities">
    <p>As a city we need to rekindle that passion that made us the most modern small city in North America at the turn of the century.</p>
    <p>That means, if you currently own and operate a business large or small we need your input to improve the efficiency of how we deliver services. No more endless meetings without any results.</p>
    <p>&nbsp;If you’re in the planning stages and need assistance, the city will be there to offer support and guidance.</p>
    <p>&nbsp;Regional projects are vitality important to the flow of goods and services.</p>
    <p>As a Civic Harbor Vote I have personally spoken to the CEO’s of several new industries that have never even considered Harbor Falls before they received my call. These are leading edge technologies that have the high growth potential. Jobs and opportunities for young and old alike.</p>
  </section>
  <p class="open-for-business">Are we open for business absolutely!</p>

  <section class="panel-copy copy-community">
    <p>Without a safe community it will be difficult to attract new people and new businesses to our community.</p>
    <p>I have a plan that will utilize the resources of the current police force to better facilitate the services that are currently provided.</p>
    <p>&nbsp;Incentive programs need to be initiated in all city departments at the ground level so that good ideas don’t get lost in bureaucracy.</p>
    <p>Seniors and youth are the most vulnerable of all. I have plan that will identify those groups and make sure that those people receive the benefits that they <strong>deserve</strong>.</p>
  </section>

  <figure class="family-photo">
    <div class="family-photo-fill" role="img" aria-label="Photo of the candidate's father, age 92, seated in an arena beside a team mascot"></div>
  </figure>
  <p class="photo-caption">My Dad @ 92 with NRU Mascot</p>

  <span class="site-link link-left">www.civicharborvote.ca</span>
  <span class="site-link link-middle">www.civicharborvote.ca</span>
  <span class="site-link link-right">www.civicharborvote.ca</span>
</main>
</body>
</html>
```